Book cover for modern/pop-culture-oriented poetry collection

We need a simple, streamlined book-cover design (that'll ultimately be 1600 x 2500 pixels; 300 dpi) for a book of poems. We would like to see three elements on the cover: (1) the title in all caps (GLASSHOURS); (2) the author name in all caps (MIRA VENTO); (3) the main image (attached, slugged "glasshours image"). Image and text should be centered on the cover.

Target Market(s)

Readers of contemporary poetry

Font styles to use
Sans Serif

Requirements
Must have
• Book title, author name, attached photo
Nice to have
• Also attached is the cover of a book (HARBOUR) that is in the style/spirit of what we're looking for.

```html
<!DOCTYPE html>
<html lang="en">
<head>
<meta charset="UTF-8">
<title>Glasshours — Mira Vento</title>
<link rel="stylesheet" href="https://fonts.googleapis.com/css2?family=Roboto+Condensed:wght@400;700&display=swap">
<style>
  :root {
    --backdrop: #e9e7e3;
    --cover-paper: #fbfbfb;
    --title-ink: #0d0d0d;
    --author-ink: #8f8f8f;
    --image-light: #eef1f2;
    --image-glass: #a9b3b1;
    --image-wood: #4a3a2e;
    --image-shadow: #dfe4e6;
  }
  html, body {
    margin: 0;
    padding: 0;
    width: 1200px;
    height: 1200px;
    overflow: hidden;
    background: var(--backdrop);
  }
  .canvas {
    position: relative;
    width: 1200px;
    height: 1200px;
  }
  .book-cover {
    position: absolute;
    left: 285px;
    top: 73px;
    width: 640px;
    height: 1000px;
    background: var(--cover-paper);
    box-shadow: 0 2px 10px rgba(0,0,0,0.12);
  }
  .cover-image {
    position: absolute;
    left: 125px;
    top: 20px;
    width: 390px;
    height: 570px;
    display: block;
  }
  .book-title {
    position: absolute;
    left: 0;
    right: 0;
    top: 718px;
    margin: 0;
    text-align: center;
    font-family: "Roboto Condensed", sans-serif;
    font-weight: 700;
    font-size: 71px;
    line-height: 84px;
    letter-spacing: 0.5px;
    color: var(--title-ink);
  }
  .book-author {
    position: absolute;
    left: 0;
    right: 0;
    top: 812px;
    margin: 0;
    text-align: center;
    font-family: "Roboto Condensed", sans-serif;
    font-weight: 400;
    font-size: 37px;
    line-height: 44px;
    letter-spacing: 0.5px;
    color: var(--author-ink);
  }
</style>
</head>
<body>
  <main class="canvas">
    <section class="book-cover">
      <svg class="cover-image" viewBox="0 0 390 570" role="img" aria-label="glasshours image: a vintage wood-cabinet television set with antennas, standing on tapered legs against a white backdrop">
        <defs>
          <linearGradient id="imageTone" x1="0" y1="0" x2="0" y2="1">
            <stop offset="0%" stop-color="var(--image-light)"/>
            <stop offset="30%" stop-color="var(--image-glass)"/>
            <stop offset="55%" stop-color="var(--image-wood)"/>
            <stop offset="78%" stop-color="var(--image-shadow)"/>
            <stop offset="100%" stop-color="var(--image-light)"/>
          </linearGradient>
        </defs>
        <rect width="390" height="570" rx="6" fill="url(#imageTone)"/>
      </svg>
      <h1 class="book-title">GLASSHOURS</h1>
      <p class="book-author">MIRA VENTO</p>
    </section>
  </main>
</body>
</html>
```